New Business Card Design Project

I would like my card design to look exactly like the logo, design, layout, and print of the current attached file. The only change I would like made would be for the print to say THE KMW GROUP instead of THE HALLORAN GROUP. Basically, just replace his group name with my group name. I would also like the backgroud to be the same texture and color as the attached file. I love the dark blue lettering and house logo on the card.

I am completely open to the rest of the card design. I just want something clean and simple. Only basic contact info required on the card. Maybe just name: Kyle M Warrick and cell # 555.914.2087 and email kyle@orchidhomesagent.com

```html
<!DOCTYPE html>
<html lang="en">
<head>
<meta charset="utf-8">
<title>The KMW Group – Business Card</title>
<link rel="stylesheet" href="https://fonts.googleapis.com/css2?family=Roboto:wght@400;700&display=swap">
<style>
  :root {
    --bg: #2b2b2d;
    --paper: #f1f1f0;
    --paper-edge: #e2e2e0;
    --navy: #1e1c3d;
    --ink-muted: #6d6d72;
    --white: #ffffff;
  }
  * { box-sizing: border-box; margin: 0; padding: 0; }
  html, body {
    width: 1200px; height: 886px; overflow: hidden;
    background: var(--bg);
  }
  .canvas { position: relative; width: 1200px; height: 886px; }
  .card {
    position: absolute;
    width: 540px; height: 310px;
    background: linear-gradient(135deg, var(--paper) 0%, #f7f7f6 50%, var(--paper-edge) 100%);
    box-shadow: 0 18px 40px rgba(0,0,0,.45);
    overflow: hidden;
  }
  .card--front { left: 60px; top: 110px; }
  .card--back  { left: 600px; top: 466px; }

  /* front: company name */
  .company {
    position: absolute; right: 46px; top: 56px;
    display: flex; align-items: center; gap: 12px;
  }
  .company__square { width: 22px; height: 22px; background: var(--navy); flex: none; }
  .company__name {
    font-family: 'Roboto', sans-serif; font-weight: 700;
    font-size: 20px; line-height: 1; white-space: nowrap;
    color: var(--navy);
  }

  /* front: name band */
  .name-band {
    position: absolute; left: 0; top: 172px;
    width: 300px; height: 62px;
  }
  .name-band svg { position: absolute; inset: 0; }
  .name-band__text {
    position: relative; padding: 11px 0 0 24px;
    font-family: 'Roboto', sans-serif; color: var(--white);
  }
  .name-band__name { font-weight: 700; font-size: 19px; letter-spacing: .5px; white-space: nowrap; }
  .name-band__title { font-weight: 400; font-size: 13px; margin-top: 2px; }

  /* front: contact */
  .contact {
    position: absolute; left: 24px; top: 246px;
    list-style: none;
    font-family: 'Roboto', sans-serif; font-size: 12.5px; color: var(--ink-muted);
  }
  .contact li { display: flex; align-items: center; gap: 10px; height: 17px; white-space: nowrap; }
  .contact svg { width: 11px; height: 11px; flex: none; }

  /* back */
  .back-mark {
    position: absolute; inset: 0;
    display: flex; align-items: center; justify-content: center; gap: 16px;
  }
  .back-mark__square { width: 34px; height: 34px; background: var(--navy); flex: none; }
  .back-mark__name {
    font-family: 'Roboto', sans-serif; font-weight: 700;
    font-size: 34px; line-height: 1; white-space: nowrap; color: var(--navy);
  }
</style>
</head>
<body>
<main class="canvas">

  <section class="card card--front" aria-label="Business card front">
    <div class="company">
      <div class="company__square"></div>
      <div class="company__name">THE KMW GROUP</div>
    </div>

    <div class="name-band">
      <svg viewBox="0 0 300 62" width="300" height="62" aria-hidden="true">
        <polygon points="0,0 300,0 262,62 0,62" fill="var(--navy)"/>
      </svg>
      <div class="name-band__text">
        <div class="name-band__name">KYLE M WARRICK</div>
        <div class="name-band__title">CEO/FOUNDER</div>
      </div>
    </div>

    <ul class="contact">
      <li>
        <svg viewBox="0 0 12 12" aria-hidden="true"><rect x="3" y="0.5" width="6" height="11" rx="1" fill="none" stroke="var(--navy)"/><circle cx="6" cy="9.5" r=".7" fill="var(--navy)"/></svg>
        555.914.2087
      </li>
      <li>
        <svg viewBox="0 0 12 12" aria-hidden="true"><rect x="0.5" y="2" width="11" height="8" fill="var(--navy)"/><polyline points="0.5,2 6,7 11.5,2" fill="none" stroke="var(--white)"/></svg>
        kyle@orchidhomesagent.com
      </li>
      <li>
        <svg viewBox="0 0 12 12" aria-hidden="true"><circle cx="6" cy="6" r="5.5" fill="var(--navy)"/><ellipse cx="6" cy="6" rx="2.2" ry="5.5" fill="none" stroke="var(--white)" stroke-width=".8"/><line x1=".5" y1="6" x2="11.5" y2="6" stroke="var(--white)" stroke-width=".8"/></svg>
        www.orchidhomesagent.com
      </li>
    </ul>
  </section>

  <section class="card card--back" aria-label="Business card back">
    <div class="back-mark">
      <div class="back-mark__square"></div>
      <div class="back-mark__name">THE KMW GROUP</div>
    </div>
  </section>

</main>
</body>
</html>
```